Visitenkarte und Briefdesign
Zielgruppe
Limousinenservice (Stretchlimousinen)
Aufgabenstellung
Ich benötige eine Visitenkarte und ein Briefdesign in einer edlen Optik.
Auf folgender Seite können Informationen oder Bilder eingeholt werden
www.fahrt-glanzwerk.com
Ich mag einen Hintergrund in einer Lederoptik,( wie das Logo in Anhang, BILD x4)

```html
<!DOCTYPE html>
<html lang="de">
<head>
<meta charset="utf-8">
<title>Nobilis Fahrten – Geschäftsausstattung</title>
<link href="https://fonts.googleapis.com/css2?family=Open+Sans:wght@400;600;700&family=Tinos:wght@400;700&display=swap" rel="stylesheet">
<style>
  :root {
    --bg: #e4e4e4;
    --paper: #ffffff;
    --ink: #1e1e1e;
    --leather-dark: #0d0d0d;
    --leather-mid: #2a2a2a;
    --silver: #c9c9c9;
    --muted: #8a8a8a;
    --dot: #cfcfcf;
    --sig: #2b2f8f;
  }
  * { margin: 0; padding: 0; box-sizing: border-box; }
  html, body { width: 1200px; height: 842px; overflow: hidden; }
  body { background: var(--bg); font-family: "Open Sans", sans-serif; color: var(--ink); position: relative; }

  .leather { background: radial-gradient(ellipse at 40% 35%, var(--leather-mid), var(--leather-dark) 75%); }
  .brand-mark { display: inline-flex; align-items: center; justify-content: center; background: var(--leather-dark);
    color: var(--silver); font-family: "Open Sans", sans-serif; font-weight: 700; text-align: center; line-height: 1.1; }

  /* Notizblock */
  .notepad { position: absolute; left: 60px; top: 70px; width: 300px; height: 240px; background: var(--paper);
    box-shadow: 0 2px 6px rgba(0,0,0,.15); overflow: hidden; }
  .notepad .brand-mark { position: absolute; left: 18px; top: 16px; width: 62px; height: 44px; font-size: 9px; }
  .notepad .grid { position: absolute; left: 100px; right: 16px; top: 20px; bottom: 60px;
    background-image: radial-gradient(circle, var(--dot) 1px, transparent 1.3px); background-size: 18px 18px; }
  .notepad .url-band { position: absolute; left: 0; right: 0; bottom: 18px; height: 30px; background: var(--leather-mid);
    color: #e8e8e8; font-size: 13px; letter-spacing: 3px; display: flex; align-items: center; justify-content: flex-end; padding-right: 22px; }

  /* Visitenkarten */
  .card { position: absolute; width: 340px; height: 196px; box-shadow: 0 2px 6px rgba(0,0,0,.25); color: #eee; overflow: hidden; }
  .card-front { left: 40px; top: 345px; }
  .card-back { left: 40px; top: 570px; }
  .card-front .photo { position: absolute; left: 16px; top: 70px; width: 165px; height: 100px; border-radius: 6px;
    background: linear-gradient(160deg, #f4f4f4, #b9b9b9 70%, #5b5b5b); }
  .card-front .person { position: absolute; right: 18px; top: 18px; text-align: right; }
  .card-front .name { font-size: 19px; font-weight: 400; color: #fff; }
  .card-front .name b { font-weight: 700; }
  .card-front .role { font-size: 9px; color: var(--muted); }
  .card-front .rule { position: absolute; left: 18px; right: 18px; top: 60px; height: 1px; background: #555; }
  .card-front .contact { position: absolute; right: 18px; top: 72px; text-align: right; font-size: 8.5px; line-height: 1.45; color: #cfcfcf; }
  .card-back .brand-text { position: absolute; left: 0; right: 0; top: 58px; text-align: center; font-weight: 700; font-size: 28px; color: var(--silver); }
  .card-back .brand-text .dot { display: inline-block; width: 14px; height: 14px; border-radius: 50%; background: var(--silver); margin-right: 10px; vertical-align: 2px; }
  .card-back .rule { position: absolute; left: 40px; right: 40px; top: 130px; height: 1px; background: #777; }
  .card-back .tagline { position: absolute; left: 0; right: 0; top: 140px; text-align: center; font-size: 10px; letter-spacing: 1.5px; color: #ddd; font-weight: 600; }

  /* Briefbogen */
  .letter { position: absolute; left: 470px; top: 38px; width: 540px; height: 766px; background: var(--paper);
    box-shadow: 0 3px 10px rgba(0,0,0,.18); overflow: hidden; font-family: "Tinos", serif; }
  .letter .brand-mark { position: absolute; left: 235px; top: 30px; width: 80px; height: 52px; font-size: 10px; }
  .letter .sender { position: absolute; left: 60px; top: 138px; font-family: "Open Sans", sans-serif; font-size: 6.5px; color: #555; }
  .letter .fold { position: absolute; left: 0; width: 14px; height: 1px; background: #999; }
  .letter .recipient { position: absolute; left: 60px; top: 172px; font-size: 11px; line-height: 1.3; }
  .letter .subject { position: absolute; left: 60px; top: 236px; font-size: 11px; font-weight: 700; }
  .letter .body { position: absolute; left: 60px; right: 70px; top: 262px; font-size: 10.5px; line-height: 1.35; }
  .letter .body p { margin-bottom: 12px; }
  .letter .signature { position: absolute; left: 70px; top: 488px; width: 170px; height: 38px; border-radius: 4px;
    background: linear-gradient(90deg, rgba(43,47,143,.18), rgba(43,47,143,.05)); }
  .letter .signer { position: absolute; left: 104px; top: 528px; font-size: 11px; }
  .letter .footer { position: absolute; left: 0; bottom: 0; width: 540px; height: 170px; }
  .letter .footer-info { position: absolute; left: 40px; bottom: 22px; display: flex; gap: 26px; font-family: "Open Sans", sans-serif;
    font-size: 7.5px; color: #9a9a9a; line-height: 1.4; }
  .letter .footer-info .star { color: #777; }
  .letter .footer-mark { position: absolute; right: 22px; bottom: 120px; font-family: "Open Sans", sans-serif; font-weight: 700; font-size: 10px; color: var(--silver); }
</style>
</head>
<body>

  <section class="notepad">
    <div class="brand-mark">Nobilis<br>Fahrten</div>
    <div class="grid"></div>
    <div class="url-band">www.nobilis-fahrten.com</div>
  </section>

  <section class="card card-front leather">
    <div class="person">
      <div class="name"><b>Lukas</b>Brandauer</div>
      <div class="role">VIP Fahrer</div>
    </div>
    <div class="rule"></div>
    <div class="photo" role="img" aria-label="Foto einer weißen Stretchlimousine"></div>
    <div class="contact">
      l.brandauer@nobilis-fahrten.com<br>
      www.nobilis-fahrten.com<br>
      (030) 4817 256
    </div>
  </section>

  <section class="card card-back leather">
    <div class="brand-text"><span class="dot"></span>Nobilis Fahrten</div>
    <div class="rule"></div>
    <div class="tagline">GÖNNEN SIE SICH STUNDE DER EXTRAKLASSE</div>
  </section>

  <section class="letter">
    <div class="brand-mark">Nobilis<br>Fahrten</div>
    <div class="sender">Nobilis Fahrten ★ Lindenallee 14 ★ 10115 Berlin</div>
    <div class="fold" style="top:270px"></div>
    <div class="fold" style="top:540px"></div>
    <div class="recipient">Herr<br>Mustermann<br>Sonstiges<br>12345 Stadt</div>
    <div class="subject">Ihre Überschrift</div>
    <div class="body">
      <p>Lorem ipsum dolor sit amet, consetetur sadipscing elitr, sed diam nonumy eirmod tempor invidunt ut labore et dolore magna aliquyam erat, sed diam voluptua. At vero eos et accusam et justo duo dolores et ea rebum. Stet clita kasd gubergren, no sea takimata sanctus est Lorem ipsum dolor sit amet. Lorem ipsum dolor sit amet, consetetur sadipscing elitr.</p>
      <p>sed diam nonumy eirmod tempor invidunt ut labore et dolore magna aliquyam erat, sed diam voluptua. At vero eos et accusam et justo duo dolores et ea rebum. Stet clita kasd gubergren, no sea takimata sanctus est Lorem ipsum dolor sit amet. Lorem ipsum dolor sit amet, consetetur sadipscing elitr, sed diam nonumy eirmod tempor invidunt ut labore et dolore magna aliquyam erat, sed diam voluptua. At vero eos et accusam et justo duo dolores et ea rebum. Stet clita kasd gubergren.</p>
      <p>no sea takimata sanctus est Lorem ipsum dolor sit amet. Lorem ipsum dolor sit amet, consetetur sadipscing elitr, sed diam nonumy eirmod tempor invidunt ut labore et dolore magna aliquyam erat, sed diam voluptua. At vero eos et accusam et justo duo dolores et ea rebum. Stet clita kasd gubergren, no sea takimata sanctus est Lorem ipsum dolor sit amet.</p>
    </div>
    <div class="signature" role="img" aria-label="Handschriftliche Unterschrift"></div>
    <div class="signer">Lukas Brandauer</div>

    <div class="footer">
      <svg width="540" height="170" viewBox="0 0 540 170" aria-hidden="true">
        <defs>
          <radialGradient id="leatherBand" cx="45%" cy="60%" r="70%">
            <stop offset="0" stop-color="#2a2a2a"/>
            <stop offset="1" stop-color="#0d0d0d"/>
          </radialGradient>
        </defs>
        <path d="M0 160 Q 300 70 540 0 L540 170 L0 170 Z" fill="url(#leatherBand)"/>
        <path d="M0 164 Q 300 76 540 8" fill="none" stroke="#6a6a6a" stroke-width="1" stroke-dasharray="3 3"/>
      </svg>
      <div class="footer-mark">Nobilis Fahrten</div>
      <div class="footer-info">
        <span class="star">★</span>
        <span>Nobilis Fahrten<br>Lukas Brandauer</span>
        <span>Lindenallee 14<br>Lindenallee 14</span>
        <span>10115 Berlin<br>10115 Berlin</span>
        <span class="star">★</span>
        <span>Nobilis Fahrten<br>Lukas Brandauer</span>
        <span>Lindenallee 14<br>10115 Berlin</span>
      </div>
    </div>
  </section>

</body>
</html>
```